BRIMWELL TAVERN FRIDAY MAY 3

Flyer design for bar/nightclub event. Trying to keep a general theme with their flyers (see below) but would like to add some neon or some pop to it.

TEXT:

Brimwell Bar & Lounge Presents

MOONTIDE FRIDAYS
GRAND OPENING EVENT

PURE HOUSE MUSIC W/

VERNOX
TOMAS VEREK
BENTLER & MAJOR DRIFT

21+
9PM-130AM
418 K STREET DAVIS CA

Target Market(s)

House/dance music crowd.

Industry/Entity Type

Night Club

Font styles to use
Sans Serif

Colors
9bcb3c
fbee3d
ffffff

Requirements
Must have
• Large DJ names
Nice to have
• General theme of the attached flyers. Neon colors that stick with the theme. Anything else that looks cool will be considered

```html
<!DOCTYPE html>
<html lang="en">
<head>
<meta charset="UTF-8">
<title>Brimwell Bar &amp; Lounge – Moontide Fridays Grand Opening</title>
<link rel="stylesheet" href="https://fonts.googleapis.com/css2?family=Roboto:wght@400;500;700&family=Roboto+Condensed:wght@700&family=Great+Vibes&display=swap">
<style>
  :root {
    --ink: #0d0707;
    --ember-deep: #3a0804;
    --ember: #b8260c;
    --flame: #f2641c;
    --glow: #ffb14a;
    --smoke: #2b2322;
    --neon-green: #9bcb3c;
    --neon-yellow: #fbee3d;
    --white: #ffffff;
    --silver-dark: #6f6a68;
    --silver-light: #e9e6e3;
    --band-text: #3c3836;
    --badge-green: #1f4a2a;
  }
  * { margin: 0; padding: 0; box-sizing: border-box; }
  html, body { width: 818px; height: 1200px; overflow: hidden; background: var(--ink); }
  .flyer {
    position: relative;
    width: 818px;
    height: 1200px;
    overflow: hidden;
    background: var(--ink);
    font-family: "Roboto", Arial, sans-serif;
    color: var(--white);
  }
  .sky-art {
    position: absolute; left: 0; top: 0; width: 818px; height: 540px;
    background:
      radial-gradient(circle 190px at 470px 330px, var(--flame) 0%, var(--ember) 60%, rgba(120,20,6,0.6) 85%, transparent 100%),
      radial-gradient(ellipse 120px 70px at 40px 250px, var(--glow) 0%, var(--flame) 40%, transparent 100%),
      radial-gradient(ellipse 140px 60px at 740px 440px, var(--flame) 0%, transparent 100%),
      radial-gradient(ellipse 260px 120px at 560px 60px, var(--smoke) 0%, transparent 100%),
      linear-gradient(180deg, #141010 0%, #1e0f0c 30%, #4a0c05 70%, var(--ember-deep) 100%);
  }
  .crowd-art {
    position: absolute; left: 0; top: 540px; width: 818px; height: 380px;
    background:
      radial-gradient(ellipse 110px 150px at 520px 170px, var(--glow) 0%, var(--flame) 40%, transparent 100%),
      radial-gradient(ellipse 400px 170px at 400px 200px, var(--ember) 0%, var(--ember-deep) 60%, transparent 100%),
      linear-gradient(180deg, var(--ember-deep) 0%, #1a0604 100%);
  }
  .venue-badge {
    position: absolute; left: 60px; top: 40px; width: 240px; height: 260px;
  }
  .venue-badge svg { width: 240px; height: 260px; display: block; }
  .badge-arc { font-weight: 700; font-size: 17px; fill: var(--white); }
  .badge-name { font-weight: 700; font-size: 19px; fill: var(--badge-green); letter-spacing: 1px; }
  .badge-presents { font-weight: 700; font-size: 18px; fill: var(--white); }
  .silver-band {
    position: absolute; left: 0; width: 818px;
    background: linear-gradient(180deg, var(--silver-dark) 0%, var(--silver-light) 45%, #bdb8b4 70%, var(--silver-dark) 100%);
    color: var(--band-text);
    text-align: center;
    font-weight: 500;
  }
  .series-band {
    top: 500px; height: 44px; line-height: 44px;
    font-size: 19px; letter-spacing: 9px;
  }
  .event-title {
    position: absolute; left: 0; top: 560px; width: 818px; text-align: center;
    font-weight: 400;
  }
  .event-title-script {
    display: block;
    font-family: "Great Vibes", cursive;
    font-size: 104px; line-height: 1.1;
    color: var(--neon-green);
    text-shadow: 0 0 10px rgba(155, 203, 60, 0.55);
  }
  .event-title-sub {
    display: block; margin-top: -26px; padding-left: 250px;
    font-size: 20px; font-weight: 700; letter-spacing: 6px; color: var(--white);
  }
  .lineup {
    position: absolute; left: 0; top: 760px; width: 818px; text-align: center;
  }
  .lineup-intro {
    font-size: 19px; font-weight: 500; letter-spacing: 12px; color: var(--white);
  }
  .lineup-names {
    margin-top: 18px;
    font-family: "Roboto Condensed", Arial, sans-serif;
    font-weight: 700; font-size: 36px; letter-spacing: 0.5px;
    color: var(--neon-yellow);
    text-shadow: 0 0 8px rgba(251, 238, 61, 0.45);
  }
  .details-band {
    top: 940px; height: 130px;
    padding-top: 29px;
    font-size: 22px; letter-spacing: 8px; line-height: 36px;
  }
</style>
</head>
<body>
  <main class="flyer">
    <div class="sky-art" role="img" aria-label="Fiery red night sky with stars, smoke and a large dark antler silhouette"></div>
    <div class="crowd-art" role="img" aria-label="Photo of a crowd gathered around a glowing campfire at night"></div>

    <div class="venue-badge">
      <svg viewBox="0 0 240 260" aria-label="Brimwell Bar &amp; Lounge presents">
        <defs>
          <path id="badge-arc-path" d="M 32 140 A 88 88 0 0 1 208 140"/>
        </defs>
        <text class="badge-arc"><textPath href="#badge-arc-path" startOffset="50%" text-anchor="middle">Brimwell Bar &amp; Lounge</textPath></text>
        <circle cx="120" cy="140" r="66" fill="#ffffff"/>
        <text class="badge-name" x="120" y="136" text-anchor="middle">BRIMWELL</text>
        <text class="badge-name" x="120" y="160" text-anchor="middle">TAVERN</text>
        <text class="badge-presents" x="120" y="236" text-anchor="middle">Presents</text>
      </svg>
    </div>

    <div class="silver-band series-band">MOONTIDE FRIDAYS</div>

    <h1 class="event-title">
      <span class="event-title-script">Grand Opening</span>
      <span class="event-title-sub">EVENT</span>
    </h1>

    <section class="lineup">
      <p class="lineup-intro">PURE HOUSE MUSIC W/</p>
      <p class="lineup-names">VERNOX | TOMAS VEREK | BENTLER &amp; MAJOR DRIFT</p>
    </section>

    <div class="silver-band details-band">
      <p>21+ &nbsp;|&nbsp; 9PM-130AM</p>
      <p>418 K STREET DAVIS CA</p>
    </div>
  </main>
</body>
</html>
```